Aid, Development & Consulting Firm

Brenvale Outhwaite Consulting Pty Ltd is a small firm in Australia whose principal works in the area of aid and development. His experience is broad ranging from aid project design and evaluation; to offering security advice in running aid operations in dangerous situations. He works with governments and private firms in conducting training for personnel travelling to work in dangerous or difficult regions. He has worked for many years with NGO's (aid organisations) and consults to the WCA. He works in locations all over the globe which include trouble spots like Iraq and Sudan, to sleepier locales like Samoa and Fiji. Being on Asia's doorstep much time is spent in Asia eg Indonesia, Vietnam. He is often called on to monitor and evaluate aid projects throughtout the globe.

Target Market(s)

Government Aid Divisions eg in Oz, KerenFund; WCA; NGO's and consulting firms who work in developing countries

Industry/Entity Type

Security

Requirements
Nice to have
• Try and incorporate a global feel without being obvious i.e. no starving children as the primary work done is a step beyond obvious aid relief. Something very simple but bold and stylish as card holder is not a "touchy" feely person
Should not have
• No starving kid type scenarios. Prefer no pictures

```html
<!DOCTYPE html>
<html lang="en">
<head>
<meta charset="utf-8">
<title>Brenvale Outhwaite Consulting Pty Ltd – Business Cards</title>
<link rel="stylesheet" href="https://fonts.googleapis.com/css2?family=Arimo:wght@400;700&family=Open+Sans:wght@400;600&display=swap">
<style>
  :root {
    --stage: #d9d4cc;
    --card: #0a0a0b;
    --white: #f4f4f4;
    --muted: #d6d6d6;
    --blue: #1f6fc0;
    --blue-bright: #2a86d6;
    --blue-deep: #0c3a86;
  }
  * { box-sizing: border-box; margin: 0; padding: 0; }
  html, body { width: 1200px; height: 900px; overflow: hidden; background: var(--stage); }
  .stage { position: relative; width: 1200px; height: 900px; }

  .card {
    position: absolute;
    width: 620px;
    height: 370px;
    left: 290px;
    background: var(--card);
    border-radius: 34px;
    overflow: hidden;
    box-shadow: 0 10px 28px rgba(0,0,0,.35);
  }
  .card--front { top: 60px; }
  .card--back { top: 470px; }

  .halftone-band { position: absolute; inset: 0; }

  .logo-placeholder {
    position: absolute;
    display: flex;
    align-items: center;
    gap: 14px;
    font-family: "Arimo", Arial, sans-serif;
    font-weight: 400;
    color: var(--white);
    white-space: nowrap;
    line-height: 1;
  }
  .logo-square { width: 44px; height: 44px; background: var(--blue); flex: none; }

  .company-name {
    position: absolute;
    font-family: "Arimo", Arial, sans-serif;
    font-weight: 700;
    color: var(--white);
    text-transform: uppercase;
    white-space: nowrap;
  }

  .card--front .logo-placeholder { left: 0; right: 0; justify-content: center; top: 140px; font-size: 30px; }
  .card--front .company-name { left: 0; right: 0; text-align: center; top: 222px; font-size: 23px; }

  .card--back .logo-placeholder { left: 60px; top: 120px; font-size: 24px; }
  .card--back .logo-square { width: 36px; height: 36px; }
  .card--back .company-name { left: 44px; top: 192px; font-size: 19px; }

  .address {
    position: absolute;
    left: 78px;
    top: 238px;
    font-family: "Open Sans", Arial, sans-serif;
    font-size: 13px;
    line-height: 18px;
    color: var(--muted);
  }
  .contact-line { display: flex; align-items: center; gap: 7px; }
  .contact-line svg { width: 11px; height: 11px; flex: none; }

  .person {
    position: absolute;
    left: 430px;
    top: 64px;
    font-family: "Open Sans", Arial, sans-serif;
    color: var(--muted);
    font-size: 13px;
    line-height: 18px;
  }
  .person-name { color: var(--blue-bright); font-weight: 600; font-size: 16px; line-height: 20px; }
  .person-role { margin-bottom: 8px; }

  .accent-band {
    position: absolute;
    left: 0; right: 0; bottom: 0;
    height: 30px;
    background: var(--blue);
  }
  .accent-band-end {
    position: absolute;
    right: 0; bottom: 0;
    width: 62px; height: 30px;
    background: var(--blue-deep);
  }
</style>
</head>
<body>
<main class="stage">

  <section class="card card--front" aria-label="Card front">
    <svg class="halftone-band" width="620" height="370" role="img" aria-label="Diagonal halftone dot texture band" viewBox="0 0 620 370">
      <defs>
        <linearGradient id="bandFade" x1="0" y1="1" x2="1" y2="0">
          <stop offset="0" stop-color="#0a0a0b" stop-opacity="0"/>
          <stop offset="0.35" stop-color="#3a3c40"/>
          <stop offset="0.55" stop-color="#5a5d62"/>
          <stop offset="0.75" stop-color="#3a3c40"/>
          <stop offset="1" stop-color="#0a0a0b" stop-opacity="0"/>
        </linearGradient>
      </defs>
      <polygon points="0,250 0,140 620,20 620,130" fill="url(#bandFade)" opacity="0.75"/>
    </svg>
    <div class="logo-placeholder"><span class="logo-square"></span>Brenvale Outhwaite</div>
    <div class="company-name">Brenvale Outhwaite Consulting Pty Ltd</div>
  </section>

  <section class="card card--back" aria-label="Card back">
    <div class="logo-placeholder"><span class="logo-square"></span>Brenvale Outhwaite</div>
    <div class="company-name">Brenvale Outhwaite Consulting Pty Ltd</div>

    <div class="address">
      <p>14 Seventh Street, Kinmore Park,</p>
      <p>SA, 5099 Australia</p>
      <p class="contact-line">
        <svg viewBox="0 0 12 12" aria-hidden="true"><path d="M2.5 1 L4.5 1 L5.2 3.6 L4 4.6 C4.7 6 5.9 7.3 7.4 8 L8.4 6.8 L11 7.5 L11 9.5 C11 10.3 10.3 11 9.5 11 C5 10.6 1.4 7 1 2.5 C1 1.7 1.7 1 2.5 1Z" fill="var(--blue-bright)"/></svg>
        +61 8 5550 1842
      </p>
      <p class="contact-line">
        <svg viewBox="0 0 12 12" aria-hidden="true"><rect x="3" y="0.8" width="6" height="10.4" rx="1.2" fill="none" stroke="var(--blue-bright)" stroke-width="1.3"/></svg>
        +61 (0) 400 555 316
      </p>
    </div>

    <div class="person">
      <p class="person-name">B. Renford Outhwaite</p>
      <p class="person-role">Director</p>
      <p class="contact-line">
        <svg viewBox="0 0 12 12" aria-hidden="true"><rect x="0.7" y="2.2" width="10.6" height="7.6" fill="var(--blue-bright)"/><path d="M1 2.6 L6 6.6 L11 2.6" fill="none" stroke="#0a0a0b" stroke-width="1"/></svg>
        outhwaite@netmail.com
      </p>
      <p class="contact-line">
        <svg viewBox="0 0 12 12" aria-hidden="true"><rect x="0.7" y="2.2" width="10.6" height="7.6" fill="var(--blue-bright)"/><path d="M1 2.6 L6 6.6 L11 2.6" fill="none" stroke="#0a0a0b" stroke-width="1"/></svg>
        outhwaiteb@mailbox.com
      </p>
    </div>

    <div class="accent-band"></div>
    <div class="accent-band-end"></div>
  </section>

</main>
</body>
</html>
```